Hi,

The project is a 2 page design of a deal aggregator website, the deals grid page, and the dedicated deal page , the wireframe layout can be found on http://www.pricenook.co. Some things to consider:

1. We will keep the animation as is, i.e. when the user clicks on any of the deal, the deal details shows up in the other page
2. we definitely need to set a color palette
3. The header will reman always on top
4. We're using a technique called infinite scroll, so the footer is never visible

It's an interesting project with a different take on the ui of the deals presentation.

• i like the style of the following:
http://pinvoxa.com/shots/587210-Clock-Timer
http://pinvoxa.com/shots/640918-Bargoset
http://pinvoxa.com/shots/731064-Menu-Sketch

```html
<!DOCTYPE html>
<html lang="en">
<head>
<meta charset="utf-8">
<title>PriceNook – Deals</title>
<link href="https://fonts.googleapis.com/css2?family=PT+Sans+Narrow:wght@400;700&family=PT+Sans:wght@400;700&family=Open+Sans:wght@400;600&display=swap" rel="stylesheet">
<style>
:root{
  --page-bg:#f1f1f1;
  --red:#e0231d;
  --red-dark:#b8140f;
  --blue:#1e8fc4;
  --teal:#2a98a6;
  --green:#7fa51a;
  --ink:#2b2b2b;
  --muted:#8d8d8d;
  --card-border:#d6d6d6;
  --footer:#2e3032;
  --footer-dark:#1d1e20;
  --navy:#221f3d;
}
*{box-sizing:border-box;margin:0;padding:0}
html,body{width:1200px;height:2293px;overflow:hidden}
body{background:var(--page-bg);font-family:"PT Sans",Arial,sans-serif;color:var(--ink);position:relative}
.top-band{position:absolute;left:0;top:0;width:1200px;height:136px;background:linear-gradient(#fbfbfb,#e2e2e2);border-bottom:2px solid #9a9a9a}
.brand{position:absolute;left:120px;top:11px;width:216px;height:67px;background:#8f9193;border-radius:4px;display:flex;align-items:center;padding-left:16px;gap:10px}
.brand-mark{width:22px;height:22px;background:var(--red)}
.brand-name{font-family:"PT Sans",sans-serif;font-weight:700;font-size:34px;color:#fff;letter-spacing:-.5px}
.util-nav{position:absolute;left:810px;top:53px;width:270px;height:27px;border-radius:6px;background:linear-gradient(#9fbcbc,#6d8f90);display:flex;justify-content:center;align-items:center;gap:10px;font-size:11px;color:#fff;text-transform:uppercase}
.util-nav span+span:before{content:"|";margin-right:10px;opacity:.7}
.main-nav{position:absolute;left:99px;top:94px;width:1002px;height:40px;background:linear-gradient(#f02b22,var(--red-dark));border-radius:5px 5px 0 0;display:flex;align-items:center;font-family:"PT Sans Narrow",sans-serif;font-weight:700;font-size:16px;color:#fff}
.main-nav a{color:#fff;text-decoration:none;height:40px;line-height:40px;text-align:center;border-right:1px solid #f56a63;white-space:nowrap}
.hero{position:absolute;left:118px;top:153px;width:972px;height:325px;background:linear-gradient(#eef3f6,#c9d6de);border:1px solid #d0d6da;border-radius:4px}
.hero-art{position:absolute;left:16px;top:15px;width:332px;height:290px;border:3px solid var(--red);border-radius:10px;background:radial-gradient(circle at 40% 40%,#ffd23a,#f26b3a 45%,#2aa8c8 75%,#fff)}
.hero-title{position:absolute;left:474px;top:24px;font-weight:700;font-size:28px;color:var(--blue)}
.hero-copy{position:absolute;left:474px;top:62px;width:490px;font-family:"PT Sans Narrow",sans-serif;font-size:19px;line-height:23px;color:#222}
.hero-more{position:absolute;left:790px;top:282px;font-family:"PT Sans Narrow",sans-serif;font-weight:700;font-size:23px;color:#111}
.hero-badge{position:absolute;left:627px;top:175px}
.welcome{position:absolute;left:109px;top:493px;width:981px;height:88px;background:#fff;border:1px solid #d8d8d8;border-radius:8px}
.welcome h1{position:absolute;left:34px;top:10px;font-weight:400;font-size:28px;color:var(--red)}
.welcome p{position:absolute;left:90px;top:42px;font-size:26px;color:#666}
.sort-label{position:absolute;left:697px;top:8px;font-size:15px;color:#444}
.sort-btn{position:absolute;height:24px;background:var(--teal);color:#fff;font-size:14px;line-height:24px;padding-left:26px;border-radius:2px}
.sort-btn.active{background:#1c6f82}
.sort-btn:before{content:"";position:absolute;left:6px;top:5px;width:14px;height:14px;background:#fff;border-radius:3px}
.deal{position:absolute;width:428px;height:380px;background:#fff;border:1px solid var(--card-border);border-radius:12px;box-shadow:0 1px 4px rgba(0,0,0,.12)}
.deal h2{position:absolute;left:26px;top:14px;width:380px;font-family:"PT Sans Narrow",sans-serif;font-weight:700;font-size:13.5px;line-height:21px;color:var(--blue)}
.deal-photo{position:absolute;left:24px;top:57px;width:370px;height:242px}
.stats{position:absolute;left:37px;top:237px;display:flex;gap:8px}
.stat{width:105px;height:54px;background:#fff;text-align:center}
.stat small{display:block;font-size:10px;color:#aaa;text-transform:uppercase;padding-top:5px}
.stat b{display:block;font-family:"Open Sans",sans-serif;font-weight:400;font-size:22px;color:#2f6f8f;line-height:28px}
.track{position:absolute;left:59px;top:316px;width:287px;height:4px;background:#ddd}
.track i{position:absolute;left:0;top:0;height:4px;width:165px;background:var(--green)}
.track em{position:absolute;left:158px;top:-6px;width:16px;height:16px;border-radius:50%;border:2px solid var(--green);background:#fff}
.countdown{position:absolute;left:59px;top:332px;display:flex;align-items:flex-start}
.countdown .lead{width:74px;font-size:11px;line-height:12px;color:var(--muted);text-transform:uppercase;padding-top:14px}
.unit{width:54px;text-align:center}
.unit b{display:block;font-family:"PT Sans",sans-serif;font-weight:700;font-size:28px;color:var(--green);line-height:30px}
.unit small{display:block;font-size:10px;color:var(--muted)}
.footer{position:absolute;left:0;top:1917px;width:1200px;height:376px;background:linear-gradient(var(--footer),var(--footer-dark))}
.fcol{position:absolute;top:28px}
.fcol h3{font-weight:400;font-size:20px;color:#fff;margin-bottom:14px}
.post{width:190px;border-bottom:1px solid #777;padding-bottom:8px;margin-bottom:16px}
.post a{display:block;font-size:11px;color:#3aa6d8;text-decoration:none}
.post span{font-size:11px;color:#999}
.links h3{margin-bottom:2px;font-size:18px}
.links a{display:block;font-size:12px;line-height:14px;color:#888;text-decoration:none}
.links .grp{margin-bottom:18px}
.foot-brand{position:absolute;left:625px;top:302px;width:199px;height:57px;background:#8f9193;display:flex;align-items:center;padding-left:16px;gap:10px}
.foot-brand .brand-mark{width:20px;height:20px}
.foot-brand .brand-name{font-size:30px}
.cards{position:absolute;left:856px;top:330px;display:flex;gap:6px;align-items:center}
.cards span{width:34px;height:22px;border-radius:3px;background:#e8e8e8}
.cards em{font-style:normal;font-size:12px;color:#ddd;margin-left:8px}
.legal{position:absolute;left:140px;top:347px;font-size:11px;color:#bbb}
.legal .copy{color:var(--red);margin-right:30px}
.legal a{color:#3aa6d8;text-decoration:none;margin-right:14px}
</style>
</head>
<body>
<header>
  <div class="top-band"></div>
  <div class="brand"><span class="brand-mark"></span><span class="brand-name">pricenook</span></div>
  <nav class="util-nav"><span>Home</span><span>Widget</span><span>Delta Studio</span></nav>
  <nav class="main-nav">
    <a style="width:38px"><svg width="18" height="16" viewBox="0 0 18 16" style="vertical-align:middle"><path d="M9 1 1 8h2.5v7h4v-4h3v4h4V8H17z" fill="#fff"/></svg></a>
    <a style="width:203px">Clothing, Shoes and Jewelry</a>
    <a style="width:95px">Electronics</a>
    <a style="width:109px">Home &amp; Office</a>
    <a style="width:101px">Eat &amp; Drink</a>
    <a style="width:132px">Health &amp; Beauty</a>
    <a style="width:210px">Entertainment and Activities</a>
    <a style="width:57px;border:0">Travel</a>
  </nav>
</header>

<section class="hero">
  <div class="hero-art" role="img" aria-label="Colourful festival poster: Hue Fest, March 15th 2012, Kuponix"></div>
  <h2 class="hero-title">DEAL OF THE DAY</h2>
  <p class="hero-copy">Enjoy a musically and physically flamboyant day with paint and foam with performances by Selim Aboudar, contests and more at the Hue Fest Day for EGP 60 (Value EGP 120) Tikkora provide you with colors, foam and surprises!</p>
  <svg class="hero-badge" width="124" height="124" viewBox="0 0 124 124"><circle cx="62" cy="62" r="60" fill="var(--navy)"/><circle cx="62" cy="62" r="38" fill="#fff"/><text x="62" y="60" font-size="10" text-anchor="middle" font-family="PT Sans,sans-serif" fill="#222">152</text><text x="62" y="73" font-size="10" text-anchor="middle" font-family="PT Sans,sans-serif" fill="#222">DEALS FOUND</text></svg>
  <div class="hero-more">LEARN MORE</div>
</section>

<section class="welcome">
  <h1>Welcome to PRICENOOK</h1>
  <p>get best deals from pricenook.co</p>
  <div class="sort-label">Sort By</div>
  <span class="sort-btn" style="left:703px;top:28px;width:90px">Discount</span>
  <span class="sort-btn" style="left:802px;top:28px;width:65px">New</span>
  <span class="sort-btn active" style="left:873px;top:28px;width:86px">Popular</span>
  <span class="sort-btn" style="left:703px;top:60px;width:76px">Saving</span>
  <span class="sort-btn" style="left:793px;top:60px;width:94px">Time Left</span>
</section>

<main>
  <article class="deal" style="left:108px;top:600px">
    <h2>Lunetti Cafe: Get a FREE E-Voucher and Enjoy 40% Discount on Delightful Italian Snacks and Drinks</h2>
    <div class="deal-photo" role="img" aria-label="Pizza slices on a table" style="background:linear-gradient(135deg,#c9652a,#e6a85a 50%,#8c2f12)"></div>
    <div class="stats"><div class="stat"><small>Discount</small><b>100%</b></div><div class="stat"><small>Value</small><b>40 LE</b></div><div class="stat"><small>Price</small><b>0 LE</b></div></div>
    <div class="track"><i></i><em></em></div>
    <div class="countdown"><div class="lead">Deal ends in:</div><div class="unit"><b>01</b><small>Days</small></div><div class="unit"><b>12</b><small>Hours</small></div><div class="unit"><b>44</b><small>Mins</small></div><div class="unit"><b>57</b><small>Secs</small></div></div>
  </article>

  <article class="deal" style="left:604px;top:600px">
    <h2>EGP 50 Instead of EGP 100 for a Day Use and Delicious Lunch at the Amazing Palm Grove Village</h2>
    <div class="deal-photo" role="img" aria-label="Resort swimming pool with palm trees" style="background:linear-gradient(#6f8f5a,#2a86c8 35%,#3db0e6)"></div>
    <div class="stats"><div class="stat"><small>Discount</small><b>50%</b></div><div class="stat"><small>Value</small><b>100 LE</b></div><div class="stat"><small>Price</small><b>50 LE</b></div></div>
    <div class="track"><i></i><em></em></div>
    <div class="countdown"><div class="lead">Deal ends in:</div><div class="unit"><b>01</b><small>Days</small></div><div class="unit"><b>12</b><small>Hours</small></div><div class="unit"><b>44</b><small>Mins</small></div><div class="unit"><b>57</b><small>Secs</small></div></div>
  </article>

  <article class="deal" style="left:108px;top:1009px">
    <h2>EGP 34 Instead of EGP 69 for A Large Tasty Family Meal from Ranger Chicken in 5th Settlement and Orbit Mall (You must bring your paper</h2>
    <div class="deal-photo" role="img" aria-label="Fried chicken meal with fries on a purple menu board" style="background:linear-gradient(90deg,#5a2a7a,#8a3c8c 40%,#d9862c)"></div>
    <div class="stats"><div class="stat"><small>Discount</small><b>51%</b></div><div class="stat"><small>Value</small><b>69 LE</b></div><div class="stat"><small>Price</small><b>34 LE</b></div></div>
    <div class="track"><i></i><em></em></div>
    <div class="countdown"><div class="lead">Deal ends in:</div><div class="unit"><b>01</b><small>Days</small></div><div class="unit"><b>12</b><small>Hours</small></div><div class="unit"><b>44</b><small>Mins</small></div><div class="unit"><b>57</b><small>Secs</small></div></div>
  </article>

  <article class="deal" style="left:604px;top:1009px">
    <h2>EGP 65 Instead of EGP 130 for an Exciting and Colorful Experience Of Paintball Fun at Sandhill, You Will Also Receive a • • •</h2>
    <div class="deal-photo" role="img" aria-label="Paintball players on a sandy field" style="background:linear-gradient(90deg,#3a3430,#7a6a58 55%,#c9b899)"></div>
    <div class="stats"><div class="stat"><small>Discount</small><b>50%</b></div><div class="stat"><small>Value</small><b>130 LE</b></div><div class="stat"><small>Price</small><b>65 LE</b></div></div>
    <div class="track"><i></i><em></em></div>
    <div class="countdown"><div class="lead">Deal ends in:</div><div class="unit"><b>01</b><small>Days</small></div><div class="unit"><b>12</b><small>Hours</small></div><div class="unit"><b>44</b><small>Mins</small></div><div class="unit"><b>57</b><small>Secs</small></div></div>
  </article>

  <article class="deal" style="left:101px;top:1418px">
    <h2>EGP 35 for Mouthwatering Food, Drinks and Desserts Worth EGP 70 from Harbor Grill in Heliopolis</h2>
    <div class="deal-photo" role="img" aria-label="Grilled steak with pasta" style="background:linear-gradient(135deg,#7a3a12,#b8692e 50%,#4a2410)"></div>
    <div class="stats"><div class="stat"><small>Discount</small><b>50%</b></div><div class="stat"><small>Value</small><b>70 LE</b></div><div class="stat"><small>Price</small><b>35 LE</b></div></div>
    <div class="track"><i></i><em></em></div>
    <div class="countdown"><div class="lead">Deal ends in:</div><div class="unit"><b>01</b><small>Days</small></div><div class="unit"><b>12</b><small>Hours</small></div><div class="unit"><b>44</b><small>Mins</small></div><div class="unit"><b>57</b><small>Secs</small></div></div>
  </article>

  <article class="deal" style="left:602px;top:1418px">
    <h2>L.E 350 Instead of L.E 700 for a Romantic Dinner for Two and an Enchanting Private-Yacht Nile Cruise from River Pearl</h2>
    <div class="deal-photo" role="img" aria-label="White yacht on the river at sunset" style="background:linear-gradient(#6fa4c8,#e9eef0 45%,#2f6f96)"></div>
    <div class="stats"><div class="stat"><small>Discount</small><b>50%</b></div><div class="stat"><small>Value</small><b>700 LE</b></div><div class="stat"><small>Price</small><b>350 LE</b></div></div>
    <div class="track"><i></i><em></em></div>
    <div class="countdown"><div class="lead">Deal ends in:</div><div class="unit"><b>01</b><small>Days</small></div><div class="unit"><b>12</b><small>Hours</small></div><div class="unit"><b>44</b><small>Mins</small></div><div class="unit"><b>57</b><small>Secs</small></div></div>
  </article>
</main>

<footer class="footer">
  <div class="fcol" style="left:130px">
    <h3>From the Blog</h3>
    <div class="post"><a>Lorem ipsum dolor sit amet</a><span>Posted on 1/1/2010</span></div>
    <div class="post"><a>Lorem ipsum dolor sit amet</a><span>Posted on 1/1/2010</span></div>
    <div class="post"><a>Lorem ipsum dolor sit amet</a><span>Posted on 1/1/2010</span></div>
    <div class="post"><a>Lorem ipsum dolor sit amet</a><span>Posted on 1/1/2010</span></div>
  </div>
  <div class="fcol" style="left:376px">
    <h3>From the deals</h3>
    <div class="post"><a>Lorem ipsum dolor sit amet</a><span>Posted on 1/1/2010</span></div>
    <div class="post"><a>Lorem ipsum dolor sit amet</a><span>Posted on 1/1/2010</span></div>
    <div class="post" style="margin-top:62px"><a>Lorem ipsum dolor sit amet</a><span>Posted on 1/1/2010</span></div>
  </div>
  <div class="fcol links" style="left:629px">
    <div class="grp"><h3>More info</h3><a>Shipping policy</a><a>Warranty policy</a><a>Terms &amp; conditions</a></div>
    <div class="grp"><h3>About us</h3><a>Our story</a><a>Guarantee</a><a>Careers</a></div>
    <div class="grp"><h3>Questions?</h3><a>FAQ</a><a>Contact us</a><a>Take the tour</a></div>
  </div>
  <div class="fcol" style="left:877px"><h3>Get a Quote</h3></div>
  <svg style="position:absolute;left:838px;top:38px" width="224" height="224" viewBox="0 0 224 224"><defs><radialGradient id="glow"><stop offset=".8" stop-color="#fffbd0" stop-opacity=".5"/><stop offset="1" stop-color="#fffbd0" stop-opacity="0"/></radialGradient></defs><circle cx="112" cy="112" r="112" fill="url(#glow)"/><circle cx="112" cy="112" r="98" fill="var(--navy)" stroke="#fff" stroke-width="3"/><circle cx="112" cy="112" r="58" fill="#fff"/><text x="112" y="116" font-size="14" text-anchor="middle" font-family="PT Sans,sans-serif" fill="#222">152 DEALS FOUND</text></svg>
  <div class="foot-brand"><span class="brand-mark"></span><span class="brand-name">pricenook</span></div>
  <div class="cards"><span></span><span></span><span></span><span></span><em>X18</em></div>
  <div class="legal"><span class="copy">© 2011 DELTASTUDIO.CO</span><a>Legal</a><a>Privacy Police</a></div>
</footer>
</body>
</html>
```